Medical Waste Company with Logo

Need a business card design that targets office managers in the medical community. This card will be the front line for our sales team to market our services to the community. We would like to have email, phone number, website. Please use the logo attached to create a design that we would be proud of.

Target Market(s)

Medical Clients

Industry/Entity Type

Medical Supply

Contact Information for Business Card

Please use logo attached

Colors

Designer to choose colors to be used in the design.

Requirements
Must have
• Our logo (see attached file)
Nice to have
• Maybe a pop of some sort, raised..?

```html
<!DOCTYPE html>
<html lang="en">
<head>
<meta charset="utf-8">
<title>Northpeak Clinical Disposal – Business Card</title>
<link href="https://fonts.googleapis.com/css2?family=Roboto:wght@400;500;700&display=swap" rel="stylesheet">
<style>
  :root{
    --page:#2a2a2c;
    --card-dark:#15181c;
    --card-dark-2:#1e2226;
    --light-1:#f4f5f6;
    --light-2:#c9ccd0;
    --brand-blue:#3f6fb6;
    --text-light:#e9ebee;
    --text-muted:#b5b9be;
    --divider:#8d9196;
  }
  *{box-sizing:border-box;margin:0;padding:0}
  html,body{width:1200px;height:1101px;overflow:hidden}
  body{
    background:var(--page);
    font-family:"Roboto",Arial,sans-serif;
    display:flex;flex-direction:column;align-items:center;justify-content:center;gap:30px;
  }
  .card{
    width:900px;height:514px;position:relative;overflow:hidden;
    box-shadow:0 10px 30px rgba(0,0,0,.45);
  }
  /* back face */
  .card--back{
    background:linear-gradient(135deg,var(--card-dark-2),var(--card-dark));
    display:flex;align-items:center;justify-content:center;
  }
  .wordmark{
    display:flex;align-items:center;gap:16px;
    color:var(--brand-blue);font-weight:700;font-size:44px;letter-spacing:1px;
    text-transform:uppercase;line-height:1.1;text-align:center;
  }
  .wordmark__mark{width:26px;height:26px;background:var(--brand-blue);flex:none}
  /* front face */
  .card--front{background:var(--card-dark)}
  .front__hero{
    position:absolute;left:0;top:0;width:100%;height:282px;
    background:radial-gradient(ellipse at 55% 35%,var(--light-1) 0%,#e2e4e7 45%,var(--light-2) 100%);
    display:flex;align-items:center;justify-content:center;padding-top:20px;
  }
  .front__band{position:absolute;left:0;top:282px;width:100%;height:10px;background:var(--brand-blue)}
  .front__body{
    position:absolute;left:0;top:292px;width:100%;height:222px;
    display:flex;align-items:center;
  }
  .person{width:380px;text-align:right;padding-right:40px}
  .person__name{color:var(--brand-blue);font-weight:700;font-size:30px}
  .person__title{color:var(--text-muted);font-size:17px;margin-top:14px;letter-spacing:.5px}
  .divider{width:2px;height:166px;background:var(--divider)}
  .contacts{list-style:none;padding-left:30px;color:var(--text-light);font-size:20px}
  .contacts li{display:flex;align-items:flex-start;gap:14px;margin:6px 0;line-height:1.35}
  .icon{width:24px;height:24px;flex:none;margin-top:2px}
</style>
</head>
<body>

<section class="card card--back" aria-label="Card back">
  <div class="wordmark"><span class="wordmark__mark"></span>Northpeak Clinical Disposal</div>
</section>

<section class="card card--front" aria-label="Card front">
  <div class="front__hero" role="img" aria-label="Light grey faceted polygon background">
    <div class="wordmark"><span class="wordmark__mark"></span>Northpeak Clinical Disposal</div>
  </div>
  <div class="front__band"></div>
  <div class="front__body">
    <div class="person">
      <p class="person__name">Dana Whitfield</p>
      <p class="person__title">MANAGER</p>
    </div>
    <div class="divider"></div>
    <ul class="contacts">
      <li>
        <svg class="icon" viewBox="0 0 24 24"><circle cx="12" cy="12" r="12" fill="#3f6fb6"/><path d="M8.5 6.5l2 0 1 3-1.5 1c.6 1.4 1.6 2.4 3 3l1-1.5 3 1v2c0 .8-.7 1.5-1.5 1.5C10.3 16.5 7 13.2 7 8c0-.8.7-1.5 1.5-1.5z" fill="#15181c"/></svg>
        555-014-2290
      </li>
      <li>
        <svg class="icon" viewBox="0 0 24 24"><circle cx="12" cy="12" r="12" fill="#3f6fb6"/><rect x="6" y="8" width="12" height="8" rx="1" fill="#15181c"/><path d="M6.5 8.5l5.5 4 5.5-4" stroke="#3f6fb6" stroke-width="1.3" fill="none"/></svg>
        dana@northpeakclinical.com
      </li>
      <li>
        <svg class="icon" viewBox="0 0 24 24"><circle cx="12" cy="12" r="12" fill="#3f6fb6"/><g fill="none" stroke="#15181c" stroke-width="1.4"><circle cx="12" cy="12" r="6"/><ellipse cx="12" cy="12" rx="2.6" ry="6"/><path d="M6 12h12"/></g></svg>
        www.northpeakclinical.com
      </li>
      <li>
        <svg class="icon" viewBox="0 0 24 24"><circle cx="12" cy="12" r="12" fill="#3f6fb6"/><path d="M12 5a4.5 4.5 0 0 0-4.5 4.5C7.5 13 12 19 12 19s4.5-6 4.5-9.5A4.5 4.5 0 0 0 12 5z" fill="#15181c"/><circle cx="12" cy="9.5" r="1.7" fill="#3f6fb6"/></svg>
        <span>418 Cedar Ridge Road<br>Harbor WA 98000</span>
      </li>
    </ul>
  </div>
</section>

</body>
</html>
```